Plantwise Mechanics Partners. Needs a Business Card Design

We need a business card design for an engineering company which supplies industrial components (pumps, compressors, mechanical seals) provides repairs and services for above mentioned equipments. We offer a uniqe engineering solutions which help our customers to increase the productivness of their manufacturings, and energy savings.

Target Market(s)

Chemical and energy plants, refineries. Food industry and private consumers in a less.

Industry/Entity Type

Business

Contact Information for Business Card

Stylish and sleek design oriented on industrial area.

Requirements
Should not have
• company name shortening

```html
<!DOCTYPE html>
<html lang="uk">
<head>
<meta charset="utf-8">
<title>Plantwise Mechanics Partners — Business Card</title>
<link href="https://fonts.googleapis.com/css2?family=Ubuntu:wght@500&family=Open+Sans:ital,wght@1,400&family=Questrial&display=swap" rel="stylesheet">
<style>
  :root {
    --page-bg: #e9e4d8;
    --card-black: #0c0c0d;
    --card-charcoal: #26282a;
    --steel-light: #eef2f3;
    --steel-mid: #b9c0c3;
    --steel-dark: #8d9498;
    --text-white: #ffffff;
    --text-ink: #1d1f22;
    --brand-blue: #1b2f9c;
    --gear-dark-1: #1a1b1d;
    --gear-dark-2: #6b6f73;
    --gear-light-1: #d8dcde;
    --gear-light-2: #8f969a;
  }
  * { margin: 0; padding: 0; box-sizing: border-box; }
  html, body { width: 1200px; height: 1155px; overflow: hidden; }
  body { background: var(--page-bg); position: relative; }

  .card {
    position: absolute;
    left: 255px;
    width: 690px;
    height: 400px;
    overflow: hidden;
    box-shadow: 0 6px 18px rgba(0,0,0,.28);
  }
  .card--front { top: 150px; background: linear-gradient(100deg, var(--card-black) 0%, var(--card-charcoal) 55%, var(--card-black) 100%); }
  .card--back  { top: 600px; background: linear-gradient(115deg, var(--steel-mid) 0%, var(--steel-light) 45%, var(--steel-mid) 100%); }

  .gear-art { position: absolute; top: 0; height: 100%; }
  .card--front .gear-art {
    right: 0; width: 330px;
    background: radial-gradient(circle at 45% 40%, var(--gear-dark-2) 0%, var(--gear-dark-1) 70%);
    border-left: 3px solid #4a4d50;
  }
  .card--back .gear-art {
    left: 0; width: 330px;
    background: radial-gradient(circle at 40% 45%, var(--gear-light-1) 0%, var(--gear-light-2) 80%);
    border-right: 3px solid #f5f7f8;
  }

  .front-info {
    position: absolute; left: 40px; top: 60px; width: 330px;
    text-align: center; color: var(--text-white);
  }
  .brand-mark {
    display: block; width: 70px; height: 70px; border-radius: 50%;
    background: var(--text-white); margin: 0 auto 22px;
  }
  .company-name {
    font-family: "Ubuntu", sans-serif; font-weight: 500;
    font-size: 25px; line-height: 1.15;
  }
  .address {
    font-family: "Open Sans", sans-serif; font-style: italic;
    font-size: 17px; line-height: 1.5; margin-top: 20px;
  }
  .phones { margin-top: 22px; font-family: "Open Sans", sans-serif; font-size: 22px; }
  .phone-line { display: flex; align-items: center; justify-content: center; gap: 14px; line-height: 1.45; }
  .phone-line svg { width: 18px; height: 18px; }

  .back-brand {
    position: absolute; left: 30px; top: 135px; width: 270px; text-align: center;
  }
  .back-brand .brand-mark { background: var(--brand-blue); width: 62px; height: 62px; margin-bottom: 12px; }
  .back-brand .company-name { color: var(--brand-blue); font-size: 22px; }

  .person {
    position: absolute; left: 372px; top: 95px;
    font-family: "Questrial", sans-serif; color: var(--text-ink);
  }
  .person-name { font-size: 36px; line-height: 1.1; }
  .person-title { font-size: 18px; margin-top: 6px; letter-spacing: .5px; }
  .person-contact { margin-top: 38px; font-size: 24px; line-height: 1.35; }
</style>
</head>
<body>

<section class="card card--front">
  <div class="front-info">
    <span class="brand-mark"></span>
    <p class="company-name">Plantwise Mechanics Partners</p>
    <p class="address">пр. Заводской, д. 42 а,<br>Харків, Украина, 61200</p>
    <div class="phones">
      <p class="phone-line">
        <svg viewBox="0 0 20 20"><circle cx="10" cy="10" r="8.5" fill="none" stroke="#fff" stroke-width="1.6"/><path d="M6.5 12.5c1.5 1.5 3 2 4 1.5l1-1-1.8-1.8-.9.6c-.7-.3-1.3-.9-1.6-1.6l.6-.9L6 7.5l-1 1c-.5 1 0 2.5 1.5 4z" fill="#fff"/></svg>
        <span>057 300 12 48</span>
      </p>
      <p class="phone-line">
        <svg viewBox="0 0 20 20"><circle cx="10" cy="10" r="8.5" fill="none" stroke="#fff" stroke-width="1.6"/><path d="M6.5 12.5c1.5 1.5 3 2 4 1.5l1-1-1.8-1.8-.9.6c-.7-.3-1.3-.9-1.6-1.6l.6-.9L6 7.5l-1 1c-.5 1 0 2.5 1.5 4z" fill="#fff"/></svg>
        <span>057 300 96 31</span>
      </p>
    </div>
  </div>
  <div class="gear-art" role="img" aria-label="Dark brushed-metal illustration of interlocking gears"></div>
</section>

<section class="card card--back">
  <div class="gear-art" role="img" aria-label="Silver brushed-metal illustration of interlocking gears"></div>
  <div class="back-brand">
    <span class="brand-mark"></span>
    <p class="company-name">Plantwise Mechanics Partners</p>
  </div>
  <div class="person">
    <p class="person-name">Your Name</p>
    <p class="person-title">YOUR TITLE</p>
    <div class="person-contact">
      <p>057 300 12 48</p>
      <p>email@website.com</p>
    </div>
  </div>
</section>

</body>
</html>
```